I need a book cover related to cancer immunotherapy. It is related to cancer immunotherapy, and how patients can enhance their treatment results. It also discusses how adding cryoablation to immunotherapy increases the results as well.
I would like the cover to include a something related to cancer immunotherapy are immunology, such as a T cell, or antibody. I would like it to also include something related to cryoablation of cancer.

Target Market(s)

Cancer Patients and their families

Colors

Designer to choose colors to be used in the design.

Requirements
Must have
• Title is:
• The Lantern Harbor Uprising
• A Traveler's Map to Quiet Orchard Living
• Marcus T. Halvorsen, MD
Nice to have
• I would like something that relates to immunotherapy (maybe something that looks like an antibody). And also something that relates to cryoablation (freezing of a cancer). You can get a feel for our work on www.halvorsenridgeclinic.example

```html
<!DOCTYPE html>
<html lang="en">
<head>
<meta charset="utf-8">
<title>The Lantern Harbor Uprising — Book Cover</title>
<link rel="stylesheet" href="https://fonts.googleapis.com/css2?family=Saira+Extra+Condensed:wght@600&family=Saira+Semi+Condensed:wght@600&family=Cinzel:wght@500&display=swap">
<style>
  :root {
    --navy-deep: #0f2236;
    --navy-mid: #1a3550;
    --ink-white: #ffffff;
    --cell-blue: #3a4fd0;
    --cell-violet: #7a4aa8;
    --cell-red: #d8283a;
  }
  html, body {
    margin: 0;
    padding: 0;
    width: 800px;
    height: 1200px;
    overflow: hidden;
    background: var(--navy-deep);
  }
  .cover {
    position: relative;
    width: 800px;
    height: 1200px;
    overflow: hidden;
    background:
      radial-gradient(ellipse 420px 300px at 620px 180px, rgba(60,100,140,0.35), transparent 70%),
      radial-gradient(ellipse 380px 420px at 140px 640px, rgba(50,85,120,0.3), transparent 70%),
      radial-gradient(ellipse 500px 300px at 400px 1150px, rgba(5,15,28,0.6), transparent 70%),
      linear-gradient(180deg, var(--navy-mid) 0%, var(--navy-deep) 55%, #0c1b2c 100%);
  }
  .cover-art {
    position: absolute;
    left: 240px;
    top: 698px;
    width: 326px;
    height: 344px;
    border-radius: 50% 48% 50% 47%;
    background:
      radial-gradient(circle at 38% 40%, rgba(120,140,255,0.45), transparent 55%),
      linear-gradient(100deg, var(--cell-blue) 0%, var(--cell-blue) 45%, var(--cell-violet) 68%, var(--cell-red) 100%);
  }
  .cover-type {
    position: absolute;
    inset: 0;
    width: 800px;
    height: 1200px;
    fill: var(--ink-white);
  }
  .title-line {
    font-family: "Saira Extra Condensed", "Arial Narrow", sans-serif;
    font-weight: 600;
  }
  .subtitle-line {
    font-family: "Cinzel", "Times New Roman", serif;
    font-weight: 500;
  }
  .author-line {
    font-family: "Saira Semi Condensed", "Arial", sans-serif;
    font-weight: 600;
  }
</style>
</head>
<body>
  <main class="cover">
    <div class="cover-art" role="img" aria-label="Illustration of a textured immune cell shaded from blue to red"></div>
    <svg class="cover-type" viewBox="0 0 800 1200" xmlns="http://www.w3.org/2000/svg">
      <title>The Lantern Harbor Uprising — A Traveler's Map to Quiet Orchard Living — Marcus T. Halvorsen, MD</title>
      <g class="cover-title" text-anchor="middle">
        <text class="title-line" x="400" y="228" font-size="200" textLength="608" lengthAdjust="spacingAndGlyphs">THE LANTERN</text>
        <text class="title-line" x="400" y="364" font-size="162" textLength="420" lengthAdjust="spacingAndGlyphs">HARBOR</text>
        <text class="title-line" x="400" y="492" font-size="162" textLength="540" lengthAdjust="spacingAndGlyphs">UPRISING</text>
      </g>
      <g class="cover-subtitle" text-anchor="middle">
        <text class="subtitle-line" x="400" y="572" font-size="34" textLength="410" lengthAdjust="spacingAndGlyphs">A Traveler's Map to</text>
        <text class="subtitle-line" x="400" y="619" font-size="38" textLength="500" lengthAdjust="spacingAndGlyphs">Quiet Orchard Living</text>
      </g>
      <text class="author-line" x="400" y="1140" font-size="50" text-anchor="middle" textLength="596" lengthAdjust="spacingAndGlyphs">MARCUS T. HALVORSEN, MD</text>
    </svg>
  </main>
</body>
</html>
```